Lone Prairie Canvas & Sound Jubilee

Organization:
Lone Prairie Canvas and Sound Jubilee is a non-profit organization created by a group of anonymous donors to bring more fun, culture, and art to a small Texas town. Our mission is to promote art and music in Washington County.
The multi-day eclectic festival will feature three stages, a film, art vendors, live mural artists, and food trucks set up throughout historic downtown Brenham. The event is FREE to the public.
Goals:
We need an attractive poster to publicize the festival.
Details:
Lone Prairie Canvas and Sound Jubilee
Friday, October 14 – 16
Free admission (VIP tickets available)
Live music- 3 stages/10 bands
Film Screening
Art vendors and art walk
Live art murals
Food trucks
www.loneprairiecanvasandsoundjubilee.example
#loneprairiecanvasandsound
Requirements:
Please incorporate our festival logo attached.
Conclusion:
After selecting a poster design, we hope to continue to work with the artist to design other event materials including website splash page and rack cards using design elements from the poster.

```html
<!DOCTYPE html>
<html lang="en">
<head>
<meta charset="utf-8">
<title>Lone Prairie Canvas and Sound Jubilee</title>
<link rel="stylesheet" href="https://fonts.googleapis.com/css2?family=Rye&family=Kaushan+Script&family=Oswald:wght@500&family=IM+Fell+English+SC&display=swap">
<style>
  :root {
    --ink: #1c1c1c;
    --paper: #ffffff;
    --accent: #fff200;
    --staff-mid: #9a9a9a;
    --ghost: #e6e6e6;
  }
  html, body { margin: 0; padding: 0; overflow: hidden; background: var(--paper); }
  .poster {
    position: relative; width: 776px; height: 1200px; overflow: hidden;
    background: var(--paper); color: var(--ink);
  }
  .night { position: absolute; left: 0; top: 0; width: 776px; height: 400px; background: var(--ink); }
  .staff-art {
    position: absolute; left: 0; top: 400px; width: 776px; height: 300px;
    background: linear-gradient(180deg, var(--ink) 0%, #555 35%, var(--staff-mid) 60%, var(--paper) 100%);
  }
  .violin-art {
    position: absolute; left: 0; top: 640px; width: 776px; height: 457px;
    background: radial-gradient(ellipse 60% 55% at 30% 60%, var(--ghost) 0%, rgba(255,255,255,0) 100%);
  }
  .title { position: absolute; left: 0; width: 776px; text-align: center; margin: 0; color: var(--paper); font-weight: 400; white-space: nowrap; }
  .title-top { top: 30px; font: 58px/1 "Rye", serif; }
  .title-and { top: 112px; font: 64px/1 "Kaushan Script", cursive; color: var(--accent); }
  .title-bottom { top: 205px; font: 80px/1 "Rye", serif; }
  .divider { position: absolute; left: 100px; top: 334px; width: 604px; border-top: 5px dotted var(--paper); }
  .date {
    position: absolute; left: 0; top: 356px; width: 776px; text-align: center;
    font: 500 56px/1 "Oswald", sans-serif; color: var(--accent); letter-spacing: 1px;
  }
  .ticket {
    position: absolute; left: 104px; top: 540px; width: 296px; height: 128px;
    background: var(--accent); transform: rotate(-8deg); border-radius: 4px;
    text-align: center; color: var(--ink);
  }
  .ticket-inner {
    position: absolute; inset: 12px 18px; border: 2px dashed var(--ink);
    font-family: "Oswald", sans-serif; font-weight: 500;
  }
  .ticket-main { margin-top: 6px; font-size: 34px; line-height: 1; }
  .ticket-main span { font-size: 24px; vertical-align: 4px; }
  .ticket-sub { font-size: 26px; line-height: 1.1; }
  .ticket-note { font-size: 15px; line-height: 1.1; }
  .features { position: absolute; left: 0; top: 714px; width: 776px; margin: 0; padding: 0; list-style: none; text-align: center; }
  .features li { font: 46px/1 "IM Fell English SC", serif; height: 78px; white-space: nowrap; }
  .footer {
    position: absolute; left: 0; top: 1097px; width: 776px; height: 103px; background: var(--ink);
    color: var(--paper); text-align: center; font: 500 13px/1 "Oswald", sans-serif;
  }
  .footer-url { position: absolute; left: 0; width: 776px; top: 20px; }
  .footer-tag { position: absolute; left: 0; width: 776px; top: 48px; }
  .org-mark {
    position: absolute; right: 16px; top: 16px; width: 62px; height: 70px; background: var(--paper);
    color: var(--ink); font: 500 10px/1.15 "Oswald", sans-serif; display: flex; flex-direction: column;
    align-items: center; justify-content: center; gap: 4px; text-align: center;
  }
  .org-mark i { display: block; width: 14px; height: 14px; background: var(--ink); }
</style>
</head>
<body>
<div class="poster">
  <div class="night"></div>
  <div class="staff-art" role="img" aria-label="Sweeping musical staff with treble clef and notes"></div>
  <div class="violin-art" role="img" aria-label="Faint grey violin neck and body behind the list"></div>

  <h1 class="title title-top">Lone Prairie Canvas</h1>
  <div class="title title-and">And</div>
  <div class="title title-bottom">Sound Jubilee</div>
  <div class="divider"></div>
  <div class="date">FRIDAY, OCTOBER 14 – 16</div>

  <div class="ticket">
    <div class="ticket-inner">
      <div class="ticket-main"><span>★</span> FREE <span>★</span></div>
      <div class="ticket-sub">ADMISSION</div>
      <div class="ticket-note">(VIP TICKETS AVAILABLE)</div>
    </div>
  </div>

  <ul class="features">
    <li>Live music– 3 stages/10 bands</li>
    <li>Film Screening</li>
    <li>Art vendors and art walk</li>
    <li>Live art murals</li>
    <li>Food trucks</li>
  </ul>

  <footer class="footer">
    <div class="footer-url">WWW.LONEPRAIRIECANVASANDSOUNDJUBILEE.EXAMPLE</div>
    <div class="footer-tag">#LONEPRAIRIECANVASANDSOUND</div>
    <div class="org-mark"><i></i>Lone Prairie Jubilee</div>
  </footer>
</div>
</body>
</html>
```